The Maplewood Kids Health Centre needs a Letterhead

We are a bilingual pediatric clinic located in Montreal, Canada.

Our english name is Maplewood Kids Health Centre
Our french name is Centre médical Bellerive

We offer complete care for children including general pediatric care, pediatric specialist care such as Ear, Nose and Throat, Urology, Neurology and Adolescent Medicine. We also have paramedical specialists such as psychologists, social workers, occupational therapists, speech and language pathologists.

The letterhead must use and be harmonious with our new logo. See Design #4923293. We need two types of letterhead. One for a the Logo and both english and french names on the top and the second with the list of current staff on the left. I have uploaded two old examples for you to see. Thanks and good luck.

Industry/Entity Type

Clinic

Font styles to use
Sans Serif

Colors
3176b5
9d9d9d

Requirements
Must have
• Include our logo.
Nice to have
• Most of our printing is done in black and white. So a grayscale design is fine.
I have included a color and grayscale versions of our logo.

We prefer clean modern designs.

```html
<!DOCTYPE html>
<html lang="fr">
<head>
<meta charset="utf-8">
<title>Maplewood Kids Health Centre — Letterhead</title>
<link rel="stylesheet" href="https://fonts.googleapis.com/css2?family=Questrial&family=Nunito+Sans:wght@700&display=swap">
<style>
  :root {
    --backdrop: #e4e4e4;
    --paper: #ffffff;
    --sidebar: #efeeee;
    --ink-strong: #2e2e2e;
    --ink-soft: #555555;
    --ink-light: #8a8a8a;
    --divider: #c9c9c9;
    --mark-faint: #f5f4f4;
    --mark-side: #ffffff;
  }
  * { margin: 0; padding: 0; box-sizing: border-box; }
  html, body {
    width: 1115px; height: 1200px; overflow: hidden;
    background: var(--backdrop);
  }
  .letterhead {
    position: absolute; left: 147px; top: 20px;
    width: 820px; height: 1160px;
    background: var(--paper);
    overflow: hidden;
    box-shadow: 0 1px 4px rgba(0,0,0,.12);
    font-family: "Questrial", sans-serif;
  }
  .sidebar {
    position: absolute; left: 0; top: 0; bottom: 0; width: 165px;
    background: var(--sidebar);
    text-align: center;
    padding-top: 30px;
  }
  .sidebar-brand {
    display: flex; flex-direction: column; align-items: center;
    gap: 6px; height: 112px;
  }
  .sidebar-brand .dot {
    width: 52px; height: 52px; border-radius: 50%;
    background: var(--mark-side);
  }
  .sidebar-brand .brand-name {
    font-size: 11px; color: var(--ink-light); line-height: 1.25;
  }
  .staff-list { display: flex; flex-direction: column; gap: 16px; }
  .staff-group h3 {
    font-family: "Nunito Sans", sans-serif; font-weight: 700;
    font-size: 12.3px; line-height: 16.6px; color: var(--ink-strong);
    white-space: nowrap;
  }
  .staff-group p {
    font-size: 12.3px; line-height: 16.6px; color: var(--ink-soft);
    white-space: nowrap;
  }
  .masthead {
    position: absolute; right: 44px; top: 52px;
    display: flex; align-items: center;
    font-size: 23.5px; white-space: nowrap; letter-spacing: -0.2px;
  }
  .masthead .name-fr { color: var(--ink-light); }
  .masthead .name-en { color: var(--ink-soft); }
  .masthead .rule {
    width: 1px; height: 27px; background: var(--divider); margin: 0 6px;
  }
  .watermark {
    position: absolute; left: 351px; top: 714px;
    width: 466px; height: 466px; border-radius: 50%;
    background: var(--mark-faint);
  }
</style>
</head>
<body>
<main class="letterhead">
  <div class="watermark" aria-hidden="true"></div>

  <header class="masthead">
    <span class="name-fr">Centre médical Bellerive</span>
    <span class="rule"></span>
    <span class="name-en">Maplewood Kids Health Centre</span>
  </header>

  <aside class="sidebar">
    <div class="sidebar-brand">
      <span class="dot"></span>
      <span class="brand-name">Maplewood Kids<br>Health Centre</span>
    </div>
    <div class="staff-list">
      <section class="staff-group">
        <h3>Addresse / Address</h3>
        <p>2380 boul. des Érables</p>
        <p>Suite 100</p>
        <p>Bellerive, Qc</p>
        <p>H4X 2B7</p>
        <p>Tél. (514) 555-0148</p>
        <p>Fax. (514) 555-0176</p>
      </section>
      <section class="staff-group">
        <h3>Pédiatres / Pediatricians</h3>
        <p>H. Lindqvist</p>
        <p>J. Moreau</p>
        <p>R. Castellano</p>
        <p>D. Fournier</p>
        <p>N. Brassard</p>
        <p>M. Okafor</p>
        <p>D. Halvorsen</p>
      </section>
      <section class="staff-group">
        <h3>Neurologue / Neurologist</h3>
        <p>R. Valente</p>
      </section>
      <section class="staff-group">
        <h3>O.R.L. / E.N.T.</h3>
        <p>T. Haddad</p>
      </section>
      <section class="staff-group">
        <h3>Urologue / Urologist</h3>
        <p>R. Kowalski</p>
      </section>
      <section class="staff-group">
        <h3>Psychologues /<br>Psychologists</h3>
        <p>H. Bergeron</p>
        <p>A. Lachance</p>
        <p>Y. Dubois</p>
      </section>
      <section class="staff-group">
        <h3>Travailleuse social /<br>Social worker</h3>
        <p>S. Whitfield</p>
      </section>
      <section class="staff-group">
        <h3>Dietetiste / Dietician</h3>
        <p>L. Santoro</p>
      </section>
      <section class="staff-group">
        <h3>Gerante / Manager</h3>
        <p>C. Rinaldi</p>
      </section>
    </div>
  </aside>
</main>
</body>
</html>
```